" distribuidora no ramo do atacado e varejo (loja fisica ) nos produtos de embalagens em geral (descartáveis, festas e etc.) produtos de limpezas para (residencias , comércios e industriais ) e produtos personalizados no mesmo ramo. "

```html
<!DOCTYPE html>
<html lang="pt-BR">
<head>
<meta charset="UTF-8">
<title>Valmore Distribuidora – Adesivo</title>
<link rel="stylesheet" href="https://fonts.googleapis.com/css2?family=Montserrat:wght@400;600;700&display=swap">
<style>
  :root {
    --bg: #e9e9e9;
    --sticker: #ffffff;
    --ring: #1a1a1a;
    --brand-grey: #7d7f82;
    --brand-mark: #3aa6d8;
    --text-dark: #111111;
  }
  * { margin: 0; padding: 0; box-sizing: border-box; }
  html, body {
    width: 1200px;
    height: 1200px;
    overflow: hidden;
    background: var(--bg);
  }
  .canvas {
    position: relative;
    width: 1200px;
    height: 1200px;
    display: flex;
    align-items: center;
    justify-content: center;
  }
  .sticker {
    position: relative;
    width: 636px;
    height: 636px;
    border-radius: 50%;
    background: var(--sticker);
    box-shadow: 0 4px 14px rgba(0,0,0,0.12);
    display: flex;
    align-items: center;
    justify-content: center;
  }
  .sticker-ring {
    position: absolute;
    inset: 10px;
    border-radius: 50%;
    border: 6px solid var(--ring);
  }
  .sticker-content {
    position: relative;
    display: flex;
    flex-direction: column;
    align-items: center;
    font-family: "Montserrat", sans-serif;
    margin-top: -20px;
  }
  .brand-dot {
    width: 150px;
    height: 150px;
    border-radius: 50%;
    background: var(--brand-mark);
    margin-bottom: 22px;
  }
  .brand-name {
    font-size: 66px;
    font-weight: 700;
    color: var(--brand-grey);
    letter-spacing: 1px;
    line-height: 1;
  }
  .brand-tagline {
    margin-top: 10px;
    font-size: 20px;
    font-weight: 400;
    color: var(--brand-grey);
    letter-spacing: 12px;
    padding-left: 12px;
  }
  .contact {
    margin-top: 82px;
    display: flex;
    flex-direction: column;
    align-items: center;
    gap: 16px;
    color: var(--text-dark);
    font-weight: 600;
  }
  .contact-phone {
    font-size: 23px;
  }
  .contact-site {
    font-size: 23px;
    font-weight: 700;
    letter-spacing: 8px;
    padding-left: 8px;
  }
</style>
</head>
<body>
  <main class="canvas">
    <div class="sticker">
      <div class="sticker-ring"></div>
      <div class="sticker-content">
        <div class="brand-dot"></div>
        <h1 class="brand-name">VALMORE</h1>
        <p class="brand-tagline">DISTRIBUIDORA</p>
        <div class="contact">
          <p class="contact-phone">99 99999-0000</p>
          <p class="contact-site">www.site.com.br</p>
        </div>
      </div>
    </div>
  </main>
</body>
</html>
```